Home Remodeling company needs a business card design

we need a business card design for home remodeling company in hamilton county, indiana USA. we offers a wide range of construction services including whole house renovations, Design and Build Basements and Kitchen and Bathroom Remodeling . we would like to see designs for both site of business card that use the same color of the company logo and also including all information below :
1- Tarek Salim CEO / General Contractor
2- all company contacts Telephone numbers ( 1-888-VOLMI-15 ) ( 317-555-0192) email address ( info@volmihome.example) website ( www.volmihome.example ) and social media logos (Facebook- twitter- google plus )
3- company logo
4- licensed . insured . bonded

```html
<!DOCTYPE html>
<html lang="en">
<head>
<meta charset="utf-8">
<title>Volmi Home Remodeling – Business Card</title>
<link href="https://fonts.googleapis.com/css2?family=Arimo:wght@400;700&display=swap" rel="stylesheet">
<style>
  :root {
    --brand-red: #b82b37;
    --brand-red-bright: #d3313c;
    --charcoal: #3b3b3e;
    --charcoal-line: #2e2e30;
    --paper: #ffffff;
    --ink-grey: #5a5a5e;
    --stage: #e9e6e1;
    --photo-light: #c9ccd0;
    --photo-dark: #7d8a7a;
  }
  * { box-sizing: border-box; margin: 0; padding: 0; }
  html, body {
    width: 1200px; height: 902px; overflow: hidden;
    background: var(--stage);
    font-family: "Arimo", Arial, sans-serif;
  }
  .card {
    position: absolute; top: 296px;
    width: 540px; height: 309px;
    overflow: hidden;
    box-shadow: 0 6px 18px rgba(0,0,0,.18);
  }
  .card--front { left: 40px; background: var(--brand-red); }
  .card--back { left: 620px; background: var(--paper); }

  /* front side */
  .front-logo {
    position: absolute; inset: 0;
    display: flex; flex-direction: column; align-items: center; justify-content: center;
    color: var(--paper);
  }
  .front-logo__name {
    display: flex; align-items: center; gap: 14px;
    font-weight: 700; font-size: 96px; letter-spacing: 6px; line-height: 1;
  }
  .front-logo__mark { width: 16px; height: 16px; background: var(--paper); }
  .front-logo__tagline {
    margin-top: 10px; font-size: 20px; letter-spacing: 12px; font-weight: 400;
  }

  /* back side */
  .back-shapes { position: absolute; inset: 0; }
  .back-logo {
    position: absolute; right: 24px; top: 14px; text-align: right;
    color: var(--charcoal);
  }
  .back-logo__name {
    display: flex; align-items: center; justify-content: flex-end; gap: 8px;
    font-weight: 700; font-size: 56px; letter-spacing: 3px; line-height: 1;
  }
  .back-logo__mark { width: 10px; height: 10px; background: var(--brand-red-bright); }
  .back-logo__tagline { margin-top: 4px; font-size: 12px; letter-spacing: 7px; color: var(--ink-grey); line-height: 14px; }
  .back-logo__credentials { margin-top: 3px; font-size: 12px; letter-spacing: 1px; color: var(--ink-grey); line-height: 14px; }

  .contact {
    position: absolute; right: 14px; top: 152px; width: 230px;
    list-style: none; text-align: right; color: var(--paper);
  }
  .contact__name { font-size: 22px; color: var(--brand-red-bright); line-height: 1.1; }
  .contact__title { font-size: 16px; margin-bottom: 4px; }
  .contact__line {
    display: flex; justify-content: flex-end; align-items: center; gap: 8px;
    font-size: 14px; line-height: 24px;
  }
  .contact__icon {
    width: 15px; height: 15px; background: var(--brand-red-bright);
    display: flex; align-items: center; justify-content: center; flex: none;
  }
</style>
</head>
<body>

<section class="card card--front" aria-label="Business card front">
  <div class="front-logo">
    <div class="front-logo__name"><span class="front-logo__mark"></span>VOLMI</div>
    <div class="front-logo__tagline">HOME REMODELING</div>
  </div>
</section>

<section class="card card--back" aria-label="Business card back">
  <svg class="back-shapes" width="540" height="309" viewBox="0 0 540 309">
    <defs>
      <linearGradient id="photo-tone" x1="0" y1="0" x2="0" y2="1">
        <stop offset="0" stop-color="var(--photo-light)"/>
        <stop offset="1" stop-color="var(--photo-dark)"/>
      </linearGradient>
    </defs>
    <polygon points="0,70 300,160 300,309 0,309" fill="url(#photo-tone)"
             role="img" aria-label="Photo of a two-storey house seen through a magnifying glass"/>
    <polygon points="300,160 540,126 540,309 300,309" fill="var(--charcoal)"/>
    <line x1="0" y1="70" x2="300" y2="160" stroke="var(--charcoal-line)" stroke-width="3"/>
  </svg>

  <div class="back-logo">
    <div class="back-logo__name"><span class="back-logo__mark"></span>VOLMI</div>
    <div class="back-logo__tagline">HOME REMODELING</div>
    <div class="back-logo__credentials">LICENSED . INSURED . BONDED</div>
  </div>

  <ul class="contact">
    <li class="contact__name">Tarek Salim</li>
    <li class="contact__title">CEO / General Contractor</li>
    <li class="contact__line">1-888-VOLMI-15
      <span class="contact__icon"><svg width="10" height="10" viewBox="0 0 10 10"><path d="M2 1h2l1 2-1 1a5 5 0 0 0 2 2l1-1 2 1v2H8A7 7 0 0 1 1 2V1z" fill="#fff"/></svg></span></li>
    <li class="contact__line">317-555-0192
      <span class="contact__icon"><svg width="10" height="10" viewBox="0 0 10 10"><rect x="3" y="1" width="4" height="8" rx="1" fill="#fff"/></svg></span></li>
    <li class="contact__line">info@volmihome.example
      <span class="contact__icon"><svg width="10" height="10" viewBox="0 0 10 10"><rect x="1" y="2.5" width="8" height="5" fill="#fff"/><path d="M1 2.5l4 3 4-3" stroke="var(--brand-red-bright)" fill="none"/></svg></span></li>
    <li class="contact__line">www.volmihome.example
      <span class="contact__icon"><svg width="10" height="10" viewBox="0 0 10 10"><circle cx="5" cy="5" r="3.8" stroke="#fff" fill="none"/><path d="M1.2 5h7.6M5 1.2v7.6" stroke="#fff"/></svg></span></li>
  </ul>
</section>

</body>
</html>
```